Rovilent.com Trucking Company Website

Need a website designed (no content) for a trucking company, specializing in trucking of ocean containers (intermodal Trucking). Heavy emphasis on technology, using latest technology, providing unabated visibility and realtime information.
clean minimalist industrial website
example:
https://www.belquarn.com/

Target Market(s)

Professional Business Consumer corporate and small business

Industry/Entity Type

Trucking Company

Number of Pages Required

5+ page

Requirements
Must have
• Industrial Design, simple informative, for a busy professional to view and get the necessary information with out the distractions.
• Blog Page
• Client Log-In on the front page
• Technology page - showing our intensive investments in technology
Nice to have
• If ANY images included, MUST be USA related. Example if include an image of a truck, ensure its a USA model. Do the research.
• included our business card for sample of Logo
• Doesnt not have to be the same color schemes.
Should not have
• moving images

```html
<!DOCTYPE html>
<html lang="en">
<head>
<meta charset="utf-8">
<title>Rovilent.com — Intermodal Trucking</title>
<link rel="stylesheet" href="https://fonts.googleapis.com/css2?family=Questrial&family=Lexend:wght@500&family=Oswald:wght@700&display=swap">
<style>
  :root {
    --backdrop: #2b4a5e;
    --page: #0d0e10;
    --sky: #38b6f4;
    --sky-light: #5fd3fb;
    --sky-deep: #1e9be0;
    --accent-text: #4cc4f6;
    --ink: #0c1a22;
    --white: #ffffff;
    --chip: #8a9296;
  }
  * { margin: 0; padding: 0; box-sizing: border-box; }
  html, body { width: 960px; height: 1200px; overflow: hidden; }
  body {
    background: var(--backdrop);
    font-family: "Questrial", sans-serif;
    color: var(--white);
    position: relative;
  }
  .site { position: absolute; left: 54px; top: 0; width: 852px; height: 1200px; }
  .page { position: absolute; left: 0; top: 46px; width: 852px; height: 1154px; background: var(--page); }

  .brand-tab {
    position: absolute; left: 15px; top: 0; width: 307px; height: 89px;
    background: linear-gradient(180deg, var(--sky-light), var(--sky-deep));
    clip-path: polygon(0 8%, 3% 0, 92% 0, 100% 100%, 0 100%);
    border-radius: 10px 0 0 0;
  }
  .brand-name {
    position: absolute; left: 23px; top: 14px;
    font-size: 50px; color: var(--white); letter-spacing: 1px; line-height: 1;
  }

  .search { position: absolute; left: 659px; top: 71px; width: 186px; height: 27px; display: flex; }
  .search-field { flex: 1; background: var(--white); border-radius: 4px 0 0 4px; }
  .search-button { width: 53px; background: var(--sky); border-radius: 0 4px 4px 0; display: flex; align-items: center; justify-content: center; }

  .main-nav a {
    position: absolute; top: 142px; transform: translate(-50%, -50%);
    font-size: 17px; color: var(--white); text-decoration: none; white-space: nowrap;
  }
  .main-nav .is-active {
    left: 128px; width: 128px; height: 30px; line-height: 30px; text-align: center;
    background: var(--sky);
    clip-path: polygon(0 0, 88% 0, 100% 100%, 12% 100%);
  }

  .client-login { position: absolute; top: 210px; left: 256px; display: flex; align-items: center; }
  .login-field { width: 186px; height: 27px; background: var(--white); border-radius: 4px; margin-right: 31px; }
  .login-field + .login-field { margin-right: 15px; }
  .login-label { font-size: 17px; }

  .hero {
    position: absolute; left: 0; top: 284px; width: 852px; height: 339px;
    background: linear-gradient(160deg, #d9b07a 0%, #8fa3ae 35%, #4c7fb8 60%, #8a6a45 85%, #5b3f28 100%);
  }
  .hero-copy { position: absolute; left: 197px; top: 488px; transform: translateX(-50%); text-align: center; white-space: nowrap; }
  .hero-lead { font-size: 32px; line-height: 30px; color: var(--accent-text); }
  .hero-title { font-family: "Oswald", sans-serif; font-weight: 700; font-size: 39px; line-height: 48px; color: var(--accent-text); }

  .tagline {
    position: absolute; left: 0; top: 691px; width: 852px; text-align: center;
    font-family: "Lexend", sans-serif; font-weight: 500; font-size: 26px; line-height: 36px; color: var(--accent-text);
  }

  .site-footer { position: absolute; left: 0; top: 846px; width: 852px; height: 239px; background: var(--sky); }
  .footer-heading {
    position: absolute; top: 18px; font-size: 21px; color: var(--ink); white-space: nowrap;
  }
  .footer-heading::after {
    content: ""; position: absolute; left: -12px; right: -20px; bottom: -6px; height: 2px;
    background: linear-gradient(90deg, transparent, var(--ink) 20%, var(--ink) 80%, transparent);
  }
  .footer-links { position: absolute; top: 63px; list-style: none; }
  .footer-links li { font-size: 17px; height: 42px; color: var(--white); }
  .social { position: absolute; left: 587px; top: 61px; display: flex; gap: 10px; }
  .social-chip {
    width: 45px; height: 44px; border-radius: 6px; background: var(--chip);
    font-size: 8px; color: var(--white); display: flex; align-items: center; justify-content: center;
  }

  .rights { position: absolute; left: 26px; top: 1099px; font-size: 12px; }
  .payments {
    position: absolute; left: 602px; top: 1100px; width: 244px; height: 27px; background: var(--white);
    display: flex; justify-content: space-around; align-items: center;
    font-size: 10px; color: var(--ink);
  }
</style>
</head>
<body>
<div class="site">
  <div class="page"></div>

  <header>
    <div class="brand-tab"><span class="brand-name">Rovilent</span></div>
    <div class="search">
      <div class="search-field"></div>
      <div class="search-button">
        <svg width="22" height="20" viewBox="0 0 22 20" aria-hidden="true">
          <circle cx="8" cy="8" r="6" fill="none" stroke="#fff" stroke-width="2.5"/>
          <line x1="12.5" y1="12.5" x2="20" y2="18" stroke="#fff" stroke-width="3.5" stroke-linecap="round"/>
        </svg>
      </div>
    </div>
    <nav class="main-nav">
      <a class="is-active" href="#">Home</a>
      <a href="#" style="left:273px">Blog</a>
      <a href="#" style="left:425px">Technology</a>
      <a href="#" style="left:577px">About Us</a>
      <a href="#" style="left:727px">Contact</a>
    </nav>
    <div class="client-login">
      <div class="login-field"></div>
      <div class="login-field"></div>
      <span class="login-label">Client Log in</span>
    </div>
  </header>

  <section class="hero" role="img" aria-label="Photo of an American semi truck hauling an ocean container on a highway at sunset, with motion blur"></section>
  <div class="hero-copy">
    <div class="hero-lead">Trucking of ocean<br>containers</div>
    <div class="hero-title">Intermodal Trucking</div>
  </div>

  <p class="tagline">Heavy emphasis on technology, using latest technology,<br>providing unabated visibility and realtime information.</p>

  <footer class="site-footer">
    <h3 class="footer-heading" style="left:36px">Contact Us</h3>
    <ul class="footer-links" style="left:41px">
      <li>Lorem Ipsum</li><li>Lorem Ipsum</li><li>Lorem Ipsum</li><li>Lorem Ipsum</li>
    </ul>
    <h3 class="footer-heading" style="left:338px">Quick Links</h3>
    <ul class="footer-links" style="left:342px">
      <li>Lorem Ipsum</li><li>Lorem Ipsum</li><li>Lorem Ipsum</li><li>Lorem Ipsum</li>
    </ul>
    <h3 class="footer-heading" style="left:589px">Other Ways To Connect</h3>
    <div class="social">
      <span class="social-chip">Pingle</span>
      <span class="social-chip">Nookly</span>
      <span class="social-chip">Worknet</span>
      <span class="social-chip">Clipbay</span>
      <span class="social-chip">Callwave</span>
    </div>
  </footer>

  <p class="rights">All Right Reserved</p>
  <div class="payments">
    <span>Paynest</span><span>Cardo</span><span>Orbix</span><span>Findly</span><span>Trovex</span>
  </div>
</div>
</body>
</html>
```